BRVL web site redesign

Coastal Linkwork Systems service (BRVL) is a diverse technology company specialising in design and installation of fibre optics, network convergence and building services, for commercial clients in Australia, we required a new design of our website to attract new clients, generate sales leads, and provide information about our services to the market. The site and should have a new technology look and feel and be designed in word press. our branding colour is blue.

Target Market(s)

New developments, Construction organisations, Commercial end users, IT managers, Consultants.

Industry/Entity Type

It Company

Number of Pages Required

5+ page

Font styles to use
Sans Serif

Colors
0292cd
3176b5

Requirements
Must have
• key pages.
• Home page with some sizzle, automated pictures running through, I like the look of this competitor website http://www.tarelmesh.com.au/ good clean menus and easy to navigate.
• Services page our key services are Fibre optics, Security, Building services,Electrical. I would like the same page layout (Design) for all our services, with a find out more link on each page, manly picture driven with text around our key messaging.
• About us page with space for company profile and directors pictures, bio and contact information.
• Certifications / Accreditations page with have over 20 certifications on different products from suppliers, and a number of licences from governing bodies.
• Current and past projects page with case studies and customer outcomes
• Contact us page with options around what services they require more information on, please keep in mind the site is around generating sales Leeds and being seen as an industry expert.
Nice to have
• RSS feeds, Linked in link, to be placed within the design, Consistent BRVL branding,Same colour blue as our logo Document library for education information, white papers, presentations etc,
• a new technology look and feel, mobile friendly.
Should not have
• boring layout, move away from our cuurent website http://www.brvlgroup.com.au/
• no e eCommerce store required.

```html
<!DOCTYPE html>
<html lang="en">
<head>
<meta charset="utf-8">
<title>BRVL – Coastal Linkwork Systems service</title>
<link href="https://fonts.googleapis.com/css2?family=Arimo:wght@400;700&display=swap" rel="stylesheet">
<style>
:root{
  --blue:#0292cd;
  --blue-dark:#3176b5;
  --navy:#1d4f7d;
  --ink:#333;
  --muted:#666;
  --line:#d6d6d6;
  --panel:#f2f2f2;
  --band:#dedede;
  --footer:#3b3b3b;
  --footer-deep:#2a2a2a;
  --accent:#e07b1a;
  --red:#d0302a;
  --white:#fff;
}
*{box-sizing:border-box;margin:0;padding:0}
html,body{width:1200px;height:2706px;overflow:hidden}
body{position:relative;background:var(--white);font-family:"Arimo",Arial,sans-serif;color:var(--ink);font-size:13px;line-height:1.45}
.abs{position:absolute}
p{margin:0}

.utility{left:748px;top:0;width:277px;height:40px;background:var(--navy);display:flex;align-items:center;justify-content:space-around;color:var(--white);font-size:12px;font-weight:700;border-radius:0 0 6px 6px}
.utility span{display:flex;align-items:center;gap:6px}

.brand{left:175px;top:26px;display:flex;align-items:center;gap:14px}
.brand-mark{width:74px;height:74px;background:var(--blue)}
.brand-name{font-size:48px;font-weight:700;color:var(--blue);letter-spacing:2px}
.phone{left:555px;top:72px;display:flex;align-items:center;gap:10px;font-size:28px;font-weight:700;color:var(--navy)}
.search{left:810px;top:80px;width:215px;height:26px;display:flex}
.search-field{flex:1;border:1px solid #bbb;background:#fff;font-size:11px;color:#999;padding:5px 8px}
.search-btn{width:62px;background:var(--blue-dark);color:#fff;font-size:11px;text-align:center;line-height:26px}

.nav{left:175px;top:126px;width:850px;height:36px;background:linear-gradient(#1198d3,var(--blue-dark));display:flex;justify-content:space-between;padding:0 24px;align-items:center}
.nav a{color:#fff;font-size:13px;font-weight:700;text-decoration:none}

.hero-band{left:0;top:162px;width:1200px;height:420px;background:linear-gradient(#e9e9e9,var(--band))}
.slider{left:175px;top:180px;width:850px;height:362px;background:linear-gradient(120deg,#6c7b86 0%,#9aa9b0 35%,#4d8a6a 55%,#2f5d88 80%,#b8c2c8 100%);overflow:hidden;box-shadow:0 2px 6px rgba(0,0,0,.25)}
.slider-caption{position:absolute;left:0;right:0;top:232px;height:110px;background:rgba(20,30,40,.45);text-align:center;color:#fff;padding-top:18px}
.slider-caption h1{font-size:27px;font-weight:700;letter-spacing:.3px}
.slider-caption p{font-size:15px;margin-top:8px}
.slider-arrow{position:absolute;top:150px;width:30px;height:50px}
.slider-dots{position:absolute;left:0;right:0;bottom:10px;display:flex;justify-content:center;gap:8px}
.slider-dots i{width:10px;height:10px;border-radius:50%;background:#fff;opacity:.6}
.slider-dots i:first-child{opacity:1}

.feature{top:575px;width:272px;height:244px;background:#fff;border:1px solid var(--line)}
.feature-head{height:38px;background:linear-gradient(#1198d3,var(--blue-dark));display:flex;align-items:center;color:#fff;font-size:15px;font-weight:700}
.feature-icon{width:56px;height:38px;background:var(--navy);display:flex;align-items:center;justify-content:center;margin-right:14px}
.feature-img{margin:8px 10px 0;height:82px}
.feature-text{margin:8px 12px 0;font-size:11px;color:var(--muted);line-height:1.35}
.btn-small{position:absolute;right:12px;bottom:12px;background:var(--blue-dark);color:#fff;font-size:10px;font-weight:700;padding:5px 14px}

.welcome{left:175px;top:860px;width:560px}
.welcome h2{font-size:28px;font-weight:400;color:var(--ink)}
.welcome h2 b{color:var(--blue);font-weight:400}
.welcome p{margin-top:14px;font-size:12px;color:var(--muted);line-height:1.5}
.welcome .more{display:block;text-align:right;margin-top:12px;color:var(--accent);font-size:12px;font-weight:700}
.welcome-img{left:754px;top:858px;width:271px;height:165px;background:linear-gradient(135deg,#d7e6f2,#7fa8c9 55%,#3e6f9a);border:1px solid var(--line)}

.tabs{left:175px;top:1052px;width:850px;height:222px;background:var(--panel);border:1px solid var(--line)}
.tab-row{display:flex;border-bottom:3px solid var(--blue)}
.tab-row span{width:150px;height:40px;line-height:40px;text-align:center;font-size:13px;font-weight:700;color:#444;background:#e4e4e4;border-right:1px solid #ccc}
.tab-row span.active{background:var(--blue);color:#fff}
.thumbs{display:flex;justify-content:center;gap:38px;margin-top:44px}
.thumbs div{width:112px;height:80px;border:3px solid #fff;box-shadow:0 1px 3px rgba(0,0,0,.2)}

.about{left:175px;top:1305px;width:545px;text-align:center}
.about h2{font-size:24px;font-weight:400}
.about p{font-size:12px;color:var(--muted);line-height:1.5;margin:14px auto 0;width:300px}
.about .btn-small{position:absolute;right:0;bottom:-44px;padding:6px 16px}
.quick{left:754px;top:1305px;width:271px;height:372px;background:var(--panel);border:1px solid var(--line);padding:16px 18px}
.quick h3{color:var(--blue);font-size:19px;font-weight:700;text-align:center;margin-bottom:18px}
.field{display:flex;align-items:center;margin-bottom:14px;font-size:12px;font-weight:700}
.field label{width:75px}
.field span{flex:1;height:26px;background:#fff;border:1px solid #c8c8c8}
.field.message{align-items:flex-start}
.field.message span{height:104px}
.quick .submit{margin:4px 0 0 75px;height:28px;background:var(--blue-dark);color:#fff;font-size:12px;font-weight:700;text-align:center;line-height:28px}

.partners{left:175px;top:1718px;width:850px;text-align:center}
.partners h2{font-size:26px;font-weight:700}
.partners p{font-size:12px;color:var(--muted);margin-top:6px}
.partner-row{display:flex;justify-content:space-between;margin-top:34px;padding:0 30px}
.partner-row i{display:block;width:120px;height:40px;background:#d9d9d9;border-radius:4px}

.testimonials{left:175px;top:1968px;width:850px}
.testimonials h2{font-size:24px;font-weight:700}
.quotes{display:grid;grid-template-columns:1fr 1fr;column-gap:60px;row-gap:28px;margin-top:24px}
.quote{display:flex;gap:18px}
.avatar{flex:none;width:52px;height:52px;border-radius:50%;background:linear-gradient(#d8c7b6,#9c8775);border:2px solid #fff;box-shadow:0 0 0 1px #ccc}
.quote p{font-size:11px;color:var(--muted);line-height:1.4}
.quote .who{margin-top:8px;font-size:11px;color:var(--muted)}
.quote .who b{color:var(--red);font-weight:400}

.footer{left:0;top:2292px;width:1200px;height:414px;background:var(--footer);color:#ddd}
.footer-cols{position:absolute;left:175px;top:24px;width:850px;display:flex}
.footer-col{font-size:12px}
.footer-col h4{font-size:12px;font-weight:700;color:#fff;margin-bottom:12px;padding-bottom:6px;border-bottom:1px solid #555}
.footer-col li{list-style:none;margin-bottom:8px}
.news li{display:flex;gap:10px;margin-bottom:12px}
.news i{flex:none;width:38px;height:26px;background:linear-gradient(#7c9bb4,#48657f)}
.news span{font-size:10px;line-height:1.3;color:#ccc}
.view-all{position:absolute;left:0;width:1200px;top:216px;text-align:center;font-size:12px;color:#fff}
.newsletter{position:absolute;left:0;top:244px;width:1200px;height:138px;background:var(--footer-deep);text-align:center}
.newsletter .lead{font-size:12px;color:#ddd;padding-top:18px}
.sign-row{display:flex;justify-content:center;align-items:center;gap:12px;margin-top:12px}
.sign-row b{font-size:20px;color:#fff;font-weight:400}
.sign-row .input{width:230px;height:26px;background:#fff;color:#999;font-size:11px;text-align:left;padding:6px 8px}
.sign-row .go{background:var(--blue);color:#fff;font-size:12px;font-weight:700;padding:6px 16px}
.follow{display:flex;justify-content:center;align-items:center;gap:6px;margin-top:14px;font-size:11px;color:#ddd}
.follow i{width:18px;height:18px;background:var(--blue-dark)}
.follow span{margin-right:6px}
.copyright{position:absolute;left:0;bottom:0;width:1200px;height:32px;line-height:32px;text-align:center;font-size:11px;color:#ccc;background:#1f1f1f}
</style>
</head>
<body>

<div class="abs utility">
  <span><svg width="14" height="14" viewBox="0 0 14 14"><circle cx="7" cy="4" r="3.2" fill="#fff"/><path d="M1 14c0-4 3-6 6-6s6 2 6 6z" fill="#fff"/></svg>CLIENT LOGIN</span>
  <span><svg width="12" height="14" viewBox="0 0 12 14"><path d="M1 1h7l3 3v9H1z" stroke="#fff" stroke-width="1.5" fill="none"/><path d="M3 7h6M3 10h6" stroke="#fff" stroke-width="1.2"/></svg>GET A QUOTE</span>
</div>

<header>
  <div class="abs brand"><div class="brand-mark"></div><div class="brand-name">BRVL</div></div>
  <div class="abs phone">
    <svg width="22" height="26" viewBox="0 0 22 26"><path d="M5 1l4 6-3 3c1 4 4 7 7 9l3-3 6 4-3 5C9 25-1 13 1 4z" fill="#1d4f7d"/></svg>
    1300 555 218
  </div>
  <div class="abs search"><div class="search-field">Search</div><div class="search-btn">Search</div></div>
  <nav class="abs nav">
    <a>HOME</a><a>ABOUT US</a><a>SERVICES</a><a>ISP</a><a>RECENT PROJECTS</a><a>BLOG</a><a>CONTACT US</a>
  </nav>
</header>

<div class="abs hero-band"></div>
<section class="abs slider" role="img" aria-label="Slideshow photo of fibre optic cabling and splicing equipment">
  <svg class="slider-arrow" style="left:8px" viewBox="0 0 30 50"><path d="M22 6L8 25l14 19" stroke="#fff" stroke-width="5" fill="none"/></svg>
  <svg class="slider-arrow" style="right:8px" viewBox="0 0 30 50"><path d="M8 6l14 19L8 44" stroke="#fff" stroke-width="5" fill="none"/></svg>
  <div class="slider-caption">
    <h1>LORM IPSUM DOLOR SIT AMET, CONSECTETUR ADIPISCING</h1>
    <p>Lorem ipsum dolor sit amet, consectetur adipiscing elit. Sed diam nonummy incorrupte gravida neque.</p>
  </div>
  <div class="slider-dots"><i></i><i></i><i></i><i></i></div>
</section>

<section class="abs feature" style="left:175px">
  <div class="feature-head"><span class="feature-icon"><svg width="26" height="18" viewBox="0 0 26 18"><circle cx="8" cy="5" r="4" fill="#fff"/><circle cx="18" cy="5" r="4" fill="#fff"/><path d="M0 18c0-5 4-7 8-7s8 2 8 7zM12 18c0-5 3-7 6-7s8 2 8 7z" fill="#fff"/></svg></span>WHO WE ARE</div>
  <div class="feature-img" role="img" aria-label="Photo of a team of business people" style="background:linear-gradient(135deg,#cfd6dd,#6d7a88)"></div>
  <p class="feature-text">Lorem ipsum dolor sit amet, consecte tetur adipiscing elit. Sed diam nonummy in convallis gravida neque. Nulla gravida vestibulum metta a accumsan.</p>
  <span class="btn-small">read more</span>
</section>
<section class="abs feature" style="left:465px">
  <div class="feature-head"><span class="feature-icon"><svg width="22" height="18" viewBox="0 0 22 18"><rect x="1" y="5" width="20" height="12" fill="#fff"/><rect x="7" y="1" width="8" height="5" stroke="#fff" stroke-width="2" fill="none"/></svg></span>WHAT WE DO</div>
  <div class="feature-img" role="img" aria-label="Photo of colleagues in a meeting" style="background:linear-gradient(135deg,#e1e1e1,#7b6f66)"></div>
  <p class="feature-text">Lorem ipsum dolor sit amet, consecte tetur adipiscing elit. Sed diam nonummy in convallis gravida neque. Nulla gravida vestibulum metta a accumsan.</p>
  <span class="btn-small">read more</span>
</section>
<section class="abs feature" style="left:754px">
  <div class="feature-head"><span class="feature-icon"><svg width="20" height="20" viewBox="0 0 20 20"><path d="M3 3l14 14M17 3L3 17" stroke="#fff" stroke-width="3"/></svg></span>OUR SERVICES</div>
  <div class="feature-img" role="img" aria-label="Photo of glowing blue fibre optic strands" style="background:linear-gradient(135deg,#0a2a5a,#1d8fd8 60%,#9fe0ff)"></div>
  <p class="feature-text">Commercial Security Systems<br>Data &amp; Fibre Installations<br>Information Communication &amp; Technology<br>Electrical Fits Out</p>
  <span class="btn-small">read more</span>
</section>

<section class="abs welcome">
  <h2>Wecome to <b>BRVL.com</b></h2>
  <p>Lorem ipsum dolor sit amet, consectetur adipiscing elit. Sed diam nonummy in convallis gravida neque. Nulla gravida vestibulum metta a accumsan, aliquam in sagittis ut. Sollicitudin sed massa ut enim veniam. Curabitur tempus convallis mi vestibulum volutpat metus ante erat vestibulum. Sed aliquam dolor ut dolor consequat gravida. Fusce iaculis tempus nisi feugiat sit amet. Tincidunt ut leo. Nam semper ornare amet. Lorem ipsum dolor sit amet, consectetur adipiscing elit.</p>
  <span class="more">Read more</span>
</section>
<div class="abs welcome-img" role="img" aria-label="Photo of a businessman holding a tablet"></div>

<section class="abs tabs">
  <div class="tab-row"><span class="active">FEATURED</span><span>PROJECTS</span><span>CASE STUDIES</span></div>
  <div class="thumbs">
    <div role="img" aria-label="Photo of network hardware" style="background:linear-gradient(135deg,#b9c9d8,#53718f)"></div>
    <div role="img" aria-label="Photo of a technician at work" style="background:linear-gradient(135deg,#cfd3d6,#6b7883)"></div>
    <div role="img" aria-label="Photo of fibre optic light" style="background:linear-gradient(135deg,#0c3266,#2e8fd6)"></div>
    <div role="img" aria-label="Photo of a network patch panel" style="background:linear-gradient(135deg,#2a6fb0,#9fd2f0)"></div>
    <div role="img" aria-label="Photo of a team discussion" style="background:linear-gradient(135deg,#dedede,#7d8590)"></div>
  </div>
</section>

<section class="abs about">
  <h2>ABOUT US</h2>
  <p>Lorem ipsum dolor sit amet, consectetur adipiscing elit. Sed diam nonummy in convallis gravida neque. Nulla gravida vestibulum metta a accumsan, aliquam in sagittis ut. Sollicitudin sed massa ut enim veniam. Curabitur tempus convallis mi vestibulum volutpat metus ante erat.</p>
  <p>Lorem ipsum dolor sit amet consectetur adipiscing elit. Sed diam nonummy incorrupte gravida neque. Nulla gravida vestibulum metta a accumsan, aliquam in sagittis ut. Sed diam nonummy in convallis tempus. Nam sem per ornare amet, volutpat malesuada erat vestibulum.</p>
  <span class="btn-small">read more</span>
</section>
<section class="abs quick">
  <h3>QUICK QUESTION</h3>
  <div class="field"><label>Name</label><span></span></div>
  <div class="field"><label>Phone</label><span></span></div>
  <div class="field"><label>Email</label><span></span></div>
  <div class="field message"><label>Message</label><span></span></div>
  <div class="submit">SUBMIT</div>
</section>

<section class="abs partners">
  <h2>Our Partners</h2>
  <p>Lorem ipsum dolor sit amet, consectetur adipiscing elit. Sed diam nonummy incorrupte gravida neque.</p>
  <div class="partner-row"><i></i><i></i><i></i><i></i><i></i></div>
</section>

<section class="abs testimonials">
  <h2>What Our Customer Says</h2>
  <div class="quotes">
    <div class="quote"><div class="avatar" role="img" aria-label="Customer portrait"></div><div><p>Lorem ipsum dolor sit amet, consectetur adipiscing elit. Sed diam nonummy incorrupte gravida neque. Nulla gravida vestibulum metta a accumsan, aliquam in sagittis.</p><p class="who"><b>Lena Marsh</b>, Marketing , Bristol</p></div></div>
    <div class="quote"><div class="avatar" role="img" aria-label="Customer portrait"></div><div><p>Lorem ipsum dolor sit amet, consectetur adipiscing elit. Sed diam nonummy incorrupte gravida neque. Nulla gravida vestibulum metta a accumsan, aliquam in sagittis.</p><p class="who"><b>Owen Talbot</b>, IT Engineer , Wellington</p></div></div>
    <div class="quote"><div class="avatar" role="img" aria-label="Customer portrait"></div><div><p>Lorem ipsum dolor sit amet, consectetur adipiscing elit. Sed diam nonummy incorrupte gravida neque. Nulla gravida vestibulum metta a accumsan, aliquam in sagittis.</p><p class="who"><b>Rhys Keller</b> , Public Relations , Hobart</p></div></div>
    <div class="quote"><div class="avatar" role="img" aria-label="Customer portrait"></div><div><p>Lorem ipsum dolor sit amet, consectetur adipiscing elit. Sed diam nonummy incorrupte gravida neque. Nulla gravida vestibulum metta a accumsan, aliquam in sagittis.</p><p class="who"><b>Mara Quinn</b>, CEO, Marketing , Adelaide</p></div></div>
  </div>
</section>

<footer class="abs footer">
  <div class="footer-cols">
    <div class="footer-col" style="width:170px"><h4>MAIN MENU</h4><ul><li>Home</li><li>About Us</li><li>Services</li><li>ISP</li><li>Recent Projects</li><li>Blog</li><li>Contact Us</li></ul></div>
    <div class="footer-col news" style="width:240px;margin-left:20px"><h4>LATEST NEWS &amp; UPDATES</h4><ul>
      <li><i></i><span>January, 13th 2014 Lorem ipsum dolor sit amet nonummy</span></li>
      <li><i></i><span>February, 07th 2014 Lorem ipsum dolor sit amet nonummy</span></li>
      <li><i></i><span>March, 11th 2014 Lorem ipsum dolor sit amet nonummy</span></li>
      <li><i></i><span>March, 28th 2014 Lorem ipsum dolor sit amet nonummy</span></li>
    </ul></div>
    <div class="footer-col" style="width:170px;margin-left:40px"><h4>USEFULL LINKS</h4><ul><li>terms &amp; Conditions</li><li>Privacy policy</li><li>HELP</li><li>FAQ's</li><li>Sitemap</li></ul></div>
    <div class="footer-col" style="width:190px;margin-left:20px"><h4>OUR SERVICES</h4><ul><li>Fibre Optics</li><li>Security</li><li>Building Services</li><li>Electrical</li><li>Certifications</li></ul></div>
  </div>
  <div class="view-all">View All</div>
  <div class="newsletter">
    <p class="lead">Receive Our News &amp; update weekly, no worry about your details</p>
    <div class="sign-row"><b>NEWSLETTER</b><span class="input">Your email address</span><span class="go">SUBMIT</span></div>
    <div class="follow"><span>FOLLOW US ON</span><i></i><i></i><i></i><i></i><i></i><i></i></div>
  </div>
  <div class="copyright">Copyright © 2014 BRVL.com . All right reserved.</div>
</footer>

</body>
</html>
```